Graphic Design Project

I need to create a graphic design, which needs to be editable for me in Powerpoint... I have attached it a draft of it, but I need to be able to change the text of it. I want it to look more professional

Target Market(s)

Business Executives

Industry/Entity Type

Graphic Design

Requirements
Must have
• Make it look professional; the colors can change; I just need to be able to edit the text in powerpoint or either word

```html
<!DOCTYPE html>
<html lang="en">
<head>
<meta charset="utf-8">
<title>IT Service Pyramid – Managing Change</title>
<link rel="stylesheet" href="https://fonts.googleapis.com/css2?family=Arimo:wght@400;700&display=swap">
<style>
  :root {
    --canvas: #e4e4e4;
    --card: #ffffff;
    --orange: #f07a2a;
    --green: #44dd22;
    --yellow: #f2e23a;
    --magenta: #ee22cc;
    --slate: #8a8aa6;
    --cyan: #22c4ec;
    --sky: #2a9be6;
    --purple: #a844c8;
    --red: #e3141a;
    --metric-orange: #f2621a;
    --ink: #111111;
    --grey-text: #6e6e6e;
    --banner: #f20d0d;
  }
  * { box-sizing: border-box; margin: 0; padding: 0; }
  html, body { width: 1200px; height: 1176px; overflow: hidden; }
  body {
    background: var(--canvas);
    font-family: "Arimo", Arial, sans-serif;
    position: relative;
  }
  .tile {
    position: absolute;
    width: 238px;
    height: 198px;
    background: var(--card);
    border: 3px solid;
    border-radius: 15px;
    box-shadow: 3px 4px 8px rgba(0,0,0,0.28);
    overflow: hidden;
  }
  .tile-title {
    position: absolute;
    left: 0; right: 0;
    text-align: center;
    font-weight: 700;
    font-size: 21px;
    line-height: 1.1;
  }
  .tile-art {
    position: absolute;
    border-radius: 10px;
  }

  .vision { left: 481px; top: 110px; border-color: var(--orange); }
  .vision .tile-title { top: 10px; color: var(--ink); }
  .vision .tile-art { left: 40px; top: 72px; width: 152px; height: 108px;
    background: linear-gradient(160deg, #f4f4f4 0%, #e9e9e9 35%, #f7c27a 70%, #f29a2e 100%); }

  .operations { left: 340px; top: 324px; border-color: var(--green); }
  .operations .tile-title { top: 4px; color: var(--green); }
  .operations .rule { position: absolute; left: 46px; top: 76px; width: 142px; height: 1px; background: var(--ink); }
  .operations .tile-art { left: 44px; top: 86px; width: 146px; height: 96px;
    background: linear-gradient(90deg, #dbeefc 0%, #bfe2fa 30%, #d4f5c8 50%, #fbd2d2 72%, #f6b0b0 100%); }

  .value { left: 611px; top: 324px; border-color: var(--yellow); }
  .value .tile-title { top: 18px; color: var(--grey-text); }
  .value .tile-art { left: 36px; top: 84px; width: 160px; height: 96px;
    background: linear-gradient(160deg, #faf3df 0%, #ecd7a0 55%, #d6b05c 100%); }

  .team { left: 210px; top: 543px; border-color: var(--magenta); }
  .team .tile-title { top: 4px; color: var(--magenta); }
  .team .tile-art { left: 12px; top: 60px; width: 208px; height: 124px;
    background: linear-gradient(160deg, #fdeafa 0%, #f8d6ef 40%, #dcefc8 70%, #d4eefa 100%); }

  .relations { left: 479px; top: 543px; border-color: var(--slate); }
  .relations .tile-title { top: 8px; color: var(--slate); }
  .relations .tile-art { left: 30px; top: 86px; width: 176px; height: 98px;
    background: linear-gradient(160deg, #eef1f7 0%, #d5dbe8 50%, #f6cfa0 100%); }

  .marketing { left: 748px; top: 543px; border-color: var(--cyan); }
  .marketing .tile-title { top: 8px; left: 22px; text-align: left; color: var(--cyan); }
  .marketing .tile-art { left: 16px; top: 86px; width: 200px; height: 98px;
    background: linear-gradient(160deg, #e6f5fc 0%, #e3e6ea 50%, #bfe3f5 100%); }

  .engagement { left: 99px; top: 756px; border-color: var(--cyan); }
  .engagement .rule { position: absolute; left: 77px; top: 6px; width: 152px; height: 1px; background: var(--ink); }
  .engagement .tile-art { left: 78px; top: 14px; width: 146px; height: 94px;
    background: linear-gradient(160deg, #e4f1fc 0%, #b9dbf5 60%, #f6cfa0 100%); }
  .engagement .tile-title { top: 114px; left: 12px; text-align: left; color: var(--sky); }

  .culture { left: 355px; top: 756px; border-color: var(--purple); }
  .culture .tile-title { top: 18px; color: var(--purple); }
  .culture .tile-art { left: 30px; top: 84px; width: 176px; height: 98px;
    background: linear-gradient(160deg, #f3e6fa 0%, #e2e8fa 50%, #fbdcd6 100%); }

  .process { left: 611px; top: 756px; border-color: var(--red); }
  .process .tile-title { top: 8px; color: var(--red); }
  .process .tile-art { left: 12px; top: 66px; width: 208px; height: 118px;
    background: linear-gradient(160deg, #f2f2f2 0%, #e2e2e2 55%, #f7c8c8 100%); }

  .metrics { left: 867px; top: 756px; border-color: var(--metric-orange); }
  .metrics .tile-title { top: 28px; color: var(--metric-orange); }
  .metrics .tile-art { left: 38px; top: 72px; width: 162px; height: 110px;
    background: linear-gradient(160deg, #f4f9fc 0%, #cfe7f6 55%, #9cc9ec 100%); }

  .change-banner { position: absolute; left: 103px; top: 995px; width: 1007px; height: 70px; }
  .change-banner span {
    position: absolute; inset: 0;
    display: flex; align-items: center; justify-content: center;
    color: #fff; font-weight: 700; font-size: 40px; letter-spacing: 0.5px;
  }
</style>
</head>
<body>
  <div class="tile vision">
    <div class="tile-title">IT vision &amp;<br>Leadership</div>
    <div class="tile-art" role="img" aria-label="Illustration of a leader figure pointing forward with a team following on an orange arrow"></div>
  </div>

  <div class="tile operations">
    <div class="tile-title">Maintain IT<br>Operational<br>Excellence</div>
    <div class="rule"></div>
    <div class="tile-art" role="img" aria-label="Illustration of three coloured figures with OK tick speech bubbles"></div>
  </div>

  <div class="tile value">
    <div class="tile-title">Create<br>Business Value</div>
    <div class="tile-art" role="img" aria-label="Illustration of golden plus and percent symbols"></div>
  </div>

  <div class="tile team">
    <div class="tile-title">Transform<br>IT Team</div>
    <div class="tile-art" role="img" aria-label="Illustration of a networked group of figures with colourful speech bubbles"></div>
  </div>

  <div class="tile relations">
    <div class="tile-title">Master<br>Relationship<br>Management</div>
    <div class="tile-art" role="img" aria-label="Illustration of a circle of connected figures with one highlighted in orange"></div>
  </div>

  <div class="tile marketing">
    <div class="tile-title">Market &amp;<br>Communicate<br>Value</div>
    <div class="tile-art" role="img" aria-label="Illustration of figures assembling large letters spelling value"></div>
  </div>

  <div class="tile engagement">
    <div class="rule"></div>
    <div class="tile-art" role="img" aria-label="Illustration of figures holding up a ring of blue puzzle pieces with one orange piece"></div>
    <div class="tile-title">Customer<br>Engagement<br>Model</div>
  </div>

  <div class="tile culture">
    <div class="tile-title">Service-Minded<br>IT Culture</div>
    <div class="tile-art" role="img" aria-label="Illustration of a circle of multicoloured puzzle pieces"></div>
  </div>

  <div class="tile process">
    <div class="tile-title">Policy, Process<br>&amp; Methodologies</div>
    <div class="tile-art" role="img" aria-label="Illustration of a maze with a red arrow path leading to success"></div>
  </div>

  <div class="tile metrics">
    <div class="tile-title">Meaningful Metrics</div>
    <div class="tile-art" role="img" aria-label="Illustration of a rising blue bar chart with an orange trend arrow"></div>
  </div>

  <div class="change-banner">
    <svg width="1007" height="70" viewBox="0 0 1007 70" aria-hidden="true">
      <polygon points="0,0 1007,0 903,70 105,70" fill="var(--banner)"/>
    </svg>
    <span>MANAGING CHANGE</span>
  </div>
</body>
</html>
```